Awesome, colorful pamphlet advertising services for disabled people and supporters

My business, The Wellness Crossroads, provides nutritional counseling services to people with and without disabilities throughout the lifespan. It also offers disability consulting, body image coaching and accessible recreation consultation. I would like something representing both children and adults which ties these activities together in a happy way.

Font styles to use
Sans Serif

Colors
00AB8E
00BBA5
67D7C9
C6EFE9
E9F9F6
FFF300
FFF600
FEFA6F
FFFEC7
FFFEE8
F0912C
F2A743
F7CA91
FBE8D2
FDF5EE
E54698
E96AAD
F1A4CE
F9D9EA
FCEFF6
6B429C
8869AF
B7A5CE
E3DAEB
F3F0F8

```html
<!DOCTYPE html>
<html lang="en">
<head>
<meta charset="UTF-8">
<title>Join Our Wellness Crossroads</title>
<link href="https://fonts.googleapis.com/css2?family=Poppins:ital,wght@0,300;0,400;0,500;0,800;0,900;1,300;1,400;1,600;1,700&display=swap" rel="stylesheet">
<style>
  :root {
    --orange-deep: #e9682c;
    --orange: #f0912c;
    --orange-light: #f2a743;
    --gold: #f5b642;
    --purple: #6b429c;
    --purple-mid: #8869af;
    --magenta: #c2407f;
    --blue: #4f7cc0;
    --blue-soft: #5b82c4;
    --text: #3a3a3a;
    --panel: #f9f3f8;
    --lavender: #efedf6;
    --white: #ffffff;
  }
  * { margin: 0; padding: 0; box-sizing: border-box; }
  html, body { width: 849px; height: 1200px; overflow: hidden; background: var(--white); }
  .pamphlet {
    position: relative; width: 849px; height: 1200px; overflow: hidden;
    font-family: "Poppins", sans-serif; color: var(--text); background: var(--white);
  }
  .backdrop { position: absolute; inset: 0; }
  .headline { position: absolute; left: 44px; top: 32px; color: var(--white); line-height: 1; }
  .headline .light { display: block; font-weight: 300; font-size: 58px; letter-spacing: -1px; }
  .headline .bold { display: block; font-weight: 900; font-size: 58px; letter-spacing: -1px; margin-top: 4px; }
  .photo-slot {
    position: absolute; left: 530px; top: 290px; width: 286px; height: 286px; border-radius: 50%;
    background: radial-gradient(circle at 50% 45%, #c9a58f 0%, #8d6a55 45%, #6d6a72 75%, #ececec 100%);
    border: 4px solid var(--white);
  }
  .welcome {
    position: absolute; left: 40px; top: 458px; width: 430px;
    font-weight: 900; font-size: 26.5px; line-height: 1.25; color: var(--blue); letter-spacing: -0.6px;
  }
  .intro {
    position: absolute; left: 40px; top: 536px; width: 430px;
    font-size: 14.3px; line-height: 20px; text-align: justify; font-weight: 400;
  }
  .intro p + p.gap { margin-top: 20px; }
  .name-pill {
    position: absolute; left: 526px; top: 551px; width: 292px; height: 43px; border-radius: 22px;
    background: linear-gradient(90deg, var(--purple), var(--blue-soft));
    color: var(--white); font-weight: 700; font-style: italic; font-size: 18px;
    display: flex; align-items: center; padding-left: 18px; white-space: nowrap; overflow: hidden;
  }
  .bio {
    position: absolute; left: 540px; top: 626px; width: 271px;
    font-size: 11.6px; line-height: 14.3px; font-style: italic; font-weight: 300; text-align: justify; color: #4a4a4a;
  }
  .bio p + p { margin-top: 14.3px; }
  .certified-tag {
    position: absolute; left: 0; top: 936px; width: 88px; height: 23px;
    border-radius: 0 12px 12px 0; background: linear-gradient(90deg, var(--purple-mid), var(--blue-soft));
    color: var(--white); font-size: 14px; padding-left: 13px; line-height: 23px;
  }
  .website-label { position: absolute; left: 0; width: 290px; top: 1088px; text-align: center; font-style: italic; font-size: 14px; }
  .website-pill {
    position: absolute; left: 35px; top: 1114px; width: 220px; height: 23px; border-radius: 12px;
    background: linear-gradient(90deg, var(--purple), var(--blue-soft));
    color: var(--white); font-size: 12.5px; text-align: center; line-height: 23px; letter-spacing: 0.3px;
  }
  .footer-band {
    position: absolute; left: 0; top: 1165px; width: 849px; height: 35px;
    background: linear-gradient(90deg, var(--purple), var(--blue-soft));
  }
</style>
</head>
<body>
<div class="pamphlet">
  <svg class="backdrop" width="849" height="1200" viewBox="0 0 849 1200" aria-hidden="true">
    <defs>
      <linearGradient id="orangeBlob" x1="0" y1="0" x2="1" y2="0.3">
        <stop offset="0" stop-color="#e9682c"/>
        <stop offset="1" stop-color="#f2a743"/>
      </linearGradient>
      <linearGradient id="plumBlob" x1="0" y1="0" x2="1" y2="0">
        <stop offset="0" stop-color="#7d52a0"/>
        <stop offset="1" stop-color="#c8467e"/>
      </linearGradient>
      <linearGradient id="sunDot" x1="0" y1="0" x2="1" y2="0">
        <stop offset="0" stop-color="#ec6a2c"/>
        <stop offset="1" stop-color="#f5b642"/>
      </linearGradient>
      <linearGradient id="plumDot" x1="0" y1="0" x2="1" y2="0">
        <stop offset="0" stop-color="#6f4fa3"/>
        <stop offset="1" stop-color="#d04479"/>
      </linearGradient>
      <linearGradient id="wedge" x1="0" y1="0" x2="1" y2="1">
        <stop offset="0" stop-color="#4f7cc0"/>
        <stop offset="1" stop-color="#6b429c"/>
      </linearGradient>
      <linearGradient id="frameLine" x1="0" y1="0" x2="1" y2="0">
        <stop offset="0" stop-color="#6b429c"/>
        <stop offset="1" stop-color="#6b5ab0"/>
      </linearGradient>
    </defs>
    <rect x="512" y="390" width="337" height="775" fill="var(--panel)"/>
    <path d="M0 830 C180 760 420 800 500 960 C510 1000 512 1100 512 1165 L0 1165 Z" fill="var(--lavender)"/>
    <rect x="0" y="0" width="849" height="260" fill="url(#orangeBlob)"/>
    <path d="M0 0 L849 0 L849 150 C780 300 680 420 480 418 C300 416 120 360 0 258 Z" fill="url(#orangeBlob)"/>
    <path d="M0 258 C120 360 300 416 480 418 C600 420 700 380 780 320 L849 260 L849 400 L512 400 L512 420 C300 430 120 380 0 300 Z" fill="var(--white)"/>
    <path d="M849 0 L849 140 L740 140 C560 140 492 90 492 0 Z" fill="url(#plumBlob)"/>
    <path d="M660 140 L849 140 L849 230 C800 180 720 150 660 140 Z" fill="#f5b642"/>
    <circle cx="732" cy="199" r="52" fill="url(#sunDot)"/>
    <circle cx="800" cy="277" r="90" fill="url(#plumDot)"/>
    <polygon points="0,322 0,424 122,424" fill="url(#wedge)"/>
    <circle cx="58" cy="250" r="11" fill="var(--white)"/>
    <circle cx="92" cy="250" r="11" fill="var(--white)"/>
    <circle cx="126" cy="250" r="11" fill="var(--white)"/>
    <path d="M0 950 L288 950 A58 58 0 0 1 288 1066 L0 1066" fill="none" stroke="url(#frameLine)" stroke-width="2.5"/>
    <circle cx="78" cy="1010" r="38" fill="#8a5696" role="img" aria-label="Body image coach certification badge"/>
    <circle cx="169" cy="1010" r="38" fill="#9a9a9a" role="img" aria-label="Nutrition and lifestyle practitioner certification badge"/>
    <circle cx="169" cy="1010" r="32" fill="var(--white)"/>
    <circle cx="262" cy="1010" r="38" fill="#e8196b" role="img" aria-label="Nutrition counselor certification badge"/>
    <circle cx="262" cy="1010" r="32" fill="var(--white)"/>
  </svg>

  <h1 class="headline">
    <span class="light">JOIN OUR</span>
    <span class="bold">WELLNESS</span>
    <span class="bold">CROSSROADS!</span>
  </h1>

  <div class="photo-slot" role="img" aria-label="Portrait photo of Dana Mills"></div>

  <h2 class="welcome">WELCOME TO<br>THE WELLNESS CROSSROADS!</h2>

  <div class="intro">
    <p>I’m Dana, and I hope you find this site informative and helpful.. Here you will be able to access material on general disability issues, mental health concerns and trauma intervention as they affect disabled people and members of society at large. We are passionate about this.</p>
    <p>I provide disability aware consultation, writing, speaking and training services to businesses and organizations. Contact me to discuss your needs today!</p>
    <p class="gap">This is a place of safety, encouragement and evidence based practices. Using macro social work skills, and personal experience with physical, learning disability and chronic illness, The Wellness Crossroads seeks to help you with disability and illness related concerns and training needs.</p>
    <p>In addition to services for organizations, I provide non-clinical (not therapy) support to disabled people and supporters. If you’d like some help, contact me!</p>
  </div>

  <div class="name-pill">Dana Mills, MSW, CARSS I,</div>

  <div class="bio">
    <p>CFNC has been passionate about disability issues since 2003 when she discovered disability rights and the disability activism community. This changed her life and helped her feel stronger about herself, her disabilities, and her capabilities. In 2011, she became sick with Postural Orthostatic Tachycardia Syndrome. This was severe and life changing. It taught her about the overlap of disability and chronic illness in a way that nothing but experience can. It has been quite a journey to live with and manage. As a result, she cares about people with POTS and the wider chronic illness community and is now a certified nutrition counselor with a chronic illness emphasis.</p>
    <p>She also holds a Kindertone early childhood music and movement teacher license for babies through age seven, certification as an Adaptive Recreation and Sports Specialist from Brightfield Sports Alliance and TalkRing for seniors group facilitator certification. Lastly, she earned certificates in both working with veterans and their families from Lakeshore State University and a Trauma Informed Clinical Foundation Certificate from the Northgate University. Because she cares about trauma and body image, she is also a certified body image coach for people with and without disabilities/illness.</p>
    <p>While varied, each of these has been carefully chosen for its philosophies and contributions to The Wellness Crossroads when combined with our framework.</p>
  </div>

  <div class="certified-tag">Certified</div>

  <div class="website-label">Visit the website:</div>
  <div class="website-pill">www.wellnesscrossroads.org</div>

  <div class="footer-band"></div>
</div>
</body>
</html>
```